2-Page Flyer for the Information Session about the Tranquil Venture Course

This is a flyer to announce/advertise an evening Information Session about the Tranquil Venture Course. This Program aims at mindfully rethinking and redesigning work (and life) for people who feel stuck or not entirely satisfied with their work and/or life (please see draft flyer attached for more details). This Program is property of Brightfold Joy, a company that uses a combination of Mindfulness, Design, and Entrepreneurship to help people achieve greater happiness (in their work and lives).
Updates

Target Market(s)

People who feel stuck or not entirely satisfied with their work and/or life (please see draft flyer attached for more details)

Font styles to use
Serif
Sans Serif

Colors
ffffff
f37122
33a6d7
acd037

Requirements
Must have
• All of what I will say below is suggestive (I’m not a design expert), and I’m open to divert from it, if it makes sense and feels more interesting.
• I thought initially of a 2-page flyer (please see draft flyer attached). The first page could help people grasp the essence of the event quickly (in 1 or 2 minutes), and then, if they are interested/motivated, they would continue reading through page 2, which has more info about the Program in itself.
• Potential Structure
• Page 1
• . About the Information Session on the Tranquil Venture Course
• . Visible Date & Time, Contacts, Venue (and other relevant info)
• . About me (the facilitator)
• Page 2
• . About the Tranquil Venture Course
• I include a Powerpoint draft of the flyer with the content. The design is rudimentary and precarious from an aesthetics/organization point of view, and this is mainly where I need help (and maybe in other aspects too!).
• On the flyer, I would like to include:
• . A photo of myself (I attach 1 picture).
• . 1 or 2 beautiful-nature photos (cropped or full). One may have to do with looking at the sky, dreaming, and imagining a new work and life (2 photos with sky and clouds attached). The other has to do with walking the transformation journey (the photo with the person walking through the forest path).
• . brightfold joy logo or logos (there are two slightly different ones, that can be used for different purposes). For the first page, I would like the brightfold joy logo that has "brightfold joy" written on the bottom, with the saying "Stillness, Craft and Venture for Joy" beneath. This is the main logo. For the 2nd page, you can choose the logo that adapts better.
• - Where it says the "the way out is in" it would be great to have a similar font to the one I attach (see file "Font_the_way_out_is_in.png" and Ankecallig-fg.ttf
Nice to have
• In terms of colours, I would not divert much from the logo colours (and of course white and black). I would like the flyer to be quite white. Almost like fairy-tale white: the white horse, the white snow, the white of the stars, the white heaven. White could be the base colour. White means peace, tranquillity, calm contentment, a smile.
• And then use the other colours. The green of the mindfulness. The blue of the sky, the dreams. And the orange of the sun, the energy, the fire, the action. And maybe the black for text.
• Where it says the "the way out is in" it would be great to have a similar font to the one I attach (see file "Font_the_way_out_is_in".
• I would like this flyer to be a piece of art, in every possible way. Simple, beautiful, ease, light, peaceful, calm happy. Just like the Tranquil Venture Course and brightfold joy Company that I am creating intends to be. The mission of this Program and Company is to be a designer, a painter (a Picasso) of happier and more fulfilling human lives.
• I am very much looking forward to seeing your proposal(s).

```html
<!DOCTYPE html>
<html lang="en">
<head>
<meta charset="utf-8">
<title>Tranquil Venture Course – Information Session Flyer</title>
<link rel="stylesheet" href="https://fonts.googleapis.com/css2?family=Sacramento&family=Sue+Ellen+Francisco&family=Oswald:wght@600&family=Yanone+Kaffeesatz:wght@300;400&family=Libre+Baskerville:ital@0;1&family=Cormorant+Garamond:wght@400;500&family=Source+Sans+3:ital,wght@0,400;0,600;1,400;1,600&display=swap">
<style>
  :root {
    --white: #ffffff;
    --orange: #f37122;
    --orange-soft: #f0a070;
    --blue: #33a6d7;
    --blue-deep: #3f8ec6;
    --green: #acd037;
    --peach: #f2c4a8;
    --peach-light: #f8e1d3;
    --script: #a88f86;
    --script-light: #c9aa9e;
    --brown: #a0581e;
    --brown-soft: #b8742e;
    --ink: #3b3330;
    --ink-soft: #5a504b;
    --stage: #dcdcdc;
  }
  * { box-sizing: border-box; margin: 0; padding: 0; }
  html, body { width: 1200px; height: 952px; overflow: hidden; }
  body { background: var(--stage); position: relative; font-family: "Libre Baskerville", serif; color: var(--ink); }

  .page { position: absolute; top: 65px; width: 561px; height: 808px; overflow: hidden; background: var(--white); }
  .page--front { left: 32px; }
  .page--back { left: 625px; }
  .page > * { position: absolute; }

  .sky { inset: 0; }
  .page--front .sky {
    background:
      radial-gradient(ellipse 70% 40% at 78% 38%, rgba(255,255,255,.85), rgba(255,255,255,0) 70%),
      radial-gradient(ellipse 60% 30% at 20% 10%, rgba(255,255,255,.6), rgba(255,255,255,0) 70%),
      linear-gradient(180deg, var(--peach) 0%, var(--peach-light) 45%, #fbefe8 70%, #f6ddd0 100%);
  }
  .page--back .sky {
    background:
      radial-gradient(ellipse 60% 35% at 50% 55%, rgba(255,255,255,.9), rgba(255,255,255,0) 70%),
      linear-gradient(180deg, #fbf3ef 0%, #f6e2d7 30%, #f9ebe3 60%, #f3d6c6 100%);
  }

  /* Front page */
  .brand { left: 0; right: 0; top: 22px; display: flex; justify-content: center; align-items: center; gap: 12px; }
  .brand__dot { width: 46px; height: 46px; border-radius: 50%; background: var(--orange); }
  .brand__name { font-family: "Source Sans 3", sans-serif; font-size: 30px; color: var(--orange); line-height: 1; }
  .tagline { left: 0; right: 0; top: 78px; text-align: center; font-size: 8px; letter-spacing: 1.8px; color: #b9a39a; }
  .program-title { left: 0; right: 0; top: 96px; text-align: center; font-family: "Sacramento", cursive; font-weight: 400; font-size: 46px; letter-spacing: 5px; color: var(--script); white-space: nowrap; }

  .date-badge { left: 7px; top: 176px; width: 154px; height: 154px; border-radius: 50%; background: var(--orange-soft); opacity: .92;
    display: flex; flex-direction: column; justify-content: center; align-items: center;
    font-family: "Yanone Kaffeesatz", sans-serif; font-weight: 300; font-size: 19px; line-height: 23px; color: var(--white); text-align: center; white-space: nowrap; }

  .portrait { left: 147px; top: 166px; width: 237px; height: 330px;
    background: linear-gradient(180deg, #c9b5aa 0%, #a99a93 25%, #7f8a96 55%, rgba(190,196,204,.6) 80%, rgba(255,255,255,0) 100%);
    border-radius: 110px 110px 20px 20px; opacity: .9; }

  .facilitator { left: 405px; top: 245px; font-family: "Oswald", sans-serif; font-weight: 600; font-size: 25px; letter-spacing: 1px; color: var(--brown); }
  .facilitator-role { left: 404px; top: 281px; font-family: "Yanone Kaffeesatz", sans-serif; font-weight: 300; font-size: 14px; line-height: 14px; color: var(--brown-soft); white-space: nowrap; }

  .bio-box { left: 17px; top: 513px; width: 529px; height: 125px; border: 1px solid rgba(160,150,145,.45); }
  .facilitator-name { left: 0; right: 0; top: 486px; text-align: center; font-family: "Sacramento", cursive; font-weight: 400; font-size: 44px; line-height: 48px; color: #6f6460; white-space: nowrap; }
  .bio { left: 28px; width: 505px; font-size: 8.3px; line-height: 10.5px; color: var(--ink); text-align: center; }
  .bio--one { top: 541px; }
  .bio--two { top: 588px; }
  .bio .dropcap { font-size: 13px; }

  .info-heading { left: 37px; font-family: "Yanone Kaffeesatz", sans-serif; font-weight: 400; font-size: 15px; letter-spacing: .4px; color: var(--blue-deep); }
  .info-text { left: 37px; width: 500px; font-size: 8px; line-height: 13.5px; letter-spacing: .3px; color: var(--ink); }
  .info-heading--session { top: 650px; }
  .info-text--session { top: 670px; }
  .info-heading--access { top: 708px; }
  .info-text--access { top: 728px; }

  .contact-band { left: 0; top: 777px; width: 436px; height: 31px; }
  .contact { font-family: "Libre Baskerville", serif; font-style: italic; font-size: 7.4px; letter-spacing: .7px; color: var(--white); display: flex; align-items: center; gap: 3px; white-space: nowrap; }
  .contact svg { width: 7px; height: 7px; flex: none; }
  .contact--mail { left: 7px; top: 781px; }
  .contact--web { left: 7px; top: 792px; }
  .contact--phone { left: 232px; top: 781px; }
  .contact--pin { left: 232px; top: 792px; }
  .social { left: 440px; top: 782px; display: flex; align-items: center; gap: 5px; }
  .social__square { width: 20px; height: 20px; background: var(--blue-deep); }
  .social__handle { font-family: "Source Sans 3", sans-serif; font-style: italic; font-size: 10px; letter-spacing: 1.2px; color: var(--blue-deep); }

  /* Back page */
  .forest-path { left: 112px; top: 88px; width: 246px; height: 410px;
    background:
      radial-gradient(ellipse 25% 30% at 50% 8%, rgba(255,255,255,.95), rgba(255,255,255,0) 80%),
      radial-gradient(ellipse 30% 55% at 50% 70%, rgba(196,208,92,.75), rgba(196,208,92,0) 85%),
      linear-gradient(90deg, rgba(170,140,105,.55), rgba(190,160,120,.2) 40%, rgba(190,160,120,.2) 60%, rgba(170,140,105,.55));
    -webkit-mask-image: linear-gradient(180deg, transparent 0%, #000 12%, #000 80%, transparent 100%);
            mask-image: linear-gradient(180deg, transparent 0%, #000 12%, #000 80%, transparent 100%); }

  .motto { left: 0; right: 0; top: 12px; text-align: center; font-family: "Sacramento", cursive; font-weight: 400; font-size: 50px; letter-spacing: 3px; color: var(--script-light); white-space: nowrap; }
  .section-title { font-family: "Sue Ellen Francisco", cursive; font-weight: 400; color: var(--white); text-shadow: 0 0 1px #8d807a, 0 0 2px rgba(120,110,105,.5); line-height: 1; white-space: nowrap; }
  .section-title--what { left: 22px; top: 76px; font-size: 44px; line-height: 40px; }
  .section-title--program { left: 375px; top: 88px; font-size: 44px; }
  .section-title--why { left: 108px; top: 546px; font-size: 46px; }
  .section-title--how { left: 410px; top: 546px; font-size: 46px; }

  .prose { font-family: "Cormorant Garamond", serif; font-size: 11px; line-height: 9.8px; letter-spacing: .6px; color: var(--ink); }
  .prose--what { left: 14px; top: 176px; width: 196px; text-align: center; }
  .prose--program { left: 355px; top: 174px; width: 200px; text-align: center; }
  .prose--why { left: 12px; top: 610px; width: 240px; text-align: center; }
  .prose--why .list { text-align: left; margin-top: 8px; line-height: 11.4px; }
  .prose--why .lead { margin-top: 9px; }
  .prose--how { left: 311px; top: 610px; width: 240px; line-height: 11.4px; }
  .prose--how .center { text-align: center; line-height: 9.8px; }
  .prose--how .format { text-align: center; margin-top: 9px; line-height: 9.8px; }

  .cycle { left: 120px; top: 280px; width: 330px; height: 300px; }
  .cycle text { font-family: "Source Sans 3", sans-serif; fill: var(--white); text-anchor: middle; }
  .cycle .ws-label { font-size: 11px; }
  .cycle .ws-name { font-size: 14px; font-weight: 600; }
  .cycle .ws-hours { font-size: 10px; font-style: italic; }
  .cycle .wps { font-size: 11px; font-style: italic; font-weight: 600; fill: var(--ink-soft); text-anchor: start; }
</style>
</head>
<body>

<section class="page page--front" aria-label="Information session page">
  <div class="sky" role="img" aria-label="Soft peach sky with white clouds"></div>

  <div class="brand">
    <span class="brand__dot"></span>
    <span class="brand__name">brightfold joy</span>
  </div>
  <p class="tagline">Stillness, Craft and Venture for Joy</p>
  <h1 class="program-title">Tranquil Venture Course</h1>

  <div class="date-badge">
    <span>Thursday 18th</span>
    <span>July 2019</span>
    <span>from 19:30 to 21:00</span>
  </div>

  <div class="portrait" role="img" aria-label="Portrait photograph of the facilitator in a grey jacket and scarf"></div>

  <p class="facilitator">FACILITATOR</p>
  <p class="facilitator-role">Visiting Research<br>Fellow, University of Aldbridge</p>

  <div class="bio-box"></div>
  <h2 class="facilitator-name">Dr Marco Reis</h2>
  <p class="bio bio--one"><span class="dropcap">M</span>arco joined the University of Aldbridge (School of Management) as a Lecturer in Entrepreneurship in 015. He completed his PhD in Entrepreneurship at Kelvinside Business School (University of Kelvinside) in 2014. His dissertation received the Harrow Doctoral Dissertation Award from the Academy of Enterprise Studies.</p>
  <p class="bio bio--two">Marco began his working career in the semiconductor industry as a production engineer (Veltronic), and then in healthcare as a sales engineer (Medisant). After his MBA, he worked as a strategy consultant at Douro Business School. Originally from Portugal, Marco enjoys designing and launching new ideas, international communities,</p>

  <h3 class="info-heading info-heading--session">Information Session:</h3>
  <p class="info-text info-text--session">The purpose of this Information Session is to give you a real insight into the Tranquil Venture Course and how it can help you get the most out of your work and life.</p>
  <h3 class="info-heading info-heading--access">How much and who can come?</h3>
  <p class="info-text info-text--access">The Information Session is free and whether you come on your own, or with friends or family, you’ll be warmly welcome. It will take place on Thursday the 23rd July 2019, from 19:30 to 21:00, at Kestrel Coworking. Please get in touch for more info or to book a place.</p>

  <svg class="contact-band" viewBox="0 0 436 31" preserveAspectRatio="none" aria-hidden="true">
    <polygon points="0,0 436,0 392,31 0,31" fill="#ec8a3c"/>
  </svg>
  <p class="contact contact--mail">
    <svg viewBox="0 0 10 8"><rect x="0.5" y="0.5" width="9" height="7" fill="none" stroke="#fff"/><polyline points="0.5,0.5 5,4.5 9.5,0.5" fill="none" stroke="#fff"/></svg>
    marco.reis@brightfoldjoy.co.uk</p>
  <p class="contact contact--web">
    <svg viewBox="0 0 10 10"><circle cx="5" cy="5" r="4.3" fill="none" stroke="#fff"/><ellipse cx="5" cy="5" rx="2" ry="4.3" fill="none" stroke="#fff"/><line x1="0.7" y1="5" x2="9.3" y2="5" stroke="#fff"/></svg>
    www.brightfoldjoy.co.uk</p>
  <p class="contact contact--phone">
    <svg viewBox="0 0 6 10"><rect x="0.5" y="0.5" width="5" height="9" rx="1" fill="none" stroke="#fff"/></svg>
    +44 (0) 700 900 1234</p>
  <p class="contact contact--pin">
    <svg viewBox="0 0 8 10"><path d="M4 10 L0.8 5 A3.4 3.4 0 1 1 7.2 5 Z" fill="#fff"/><circle cx="4" cy="3.6" r="1.3" fill="#ec8a3c"/></svg>
    14 Lark Row Aldbridge AB1 2CD, Uk</p>
  <div class="social">
    <span class="social__square"></span>
    <span class="social__handle">/amarcoreis</span>
  </div>
</section>

<section class="page page--back" aria-label="Course details page">
  <div class="sky" role="img" aria-label="Pale sky with white clouds"></div>
  <div class="forest-path" role="img" aria-label="Photograph of a person walking down a sunlit forest path"></div>

  <h2 class="motto">“The Way Out is In”</h2>

  <h3 class="section-title section-title--what">What is Mindful<br>&nbsp;Entrepreneurship</h3>
  <h3 class="section-title section-title--program">The Program</h3>

  <p class="prose prose--what">Being mindful means being aware and awake. Entrepreneurship is the creation of a new form of organising. Mindful Entrepreneurship is then the process of creating or redesigning your work and life with awareness, in a way that is reflective of you, of your passions and values, thus conducing to a greater sense of fulfilment and happiness.</p>

  <p class="prose prose--program">The Tranquil Venture Course is a 4-month long transformative journey for people who feel stuck or not entirely satisfied with their work and/or life. It will be of benefit for everyone, at any stage.<br>The Program consists of a series of four 5-hour workshops, one per month, complemented by 2-hour weekly peer support meetings. It combines mindfulness techniques, design thinking methodology and entrepreneurship frameworks to achieve the desired outcomes.</p>

  <svg class="cycle" viewBox="0 0 330 300" aria-label="Cycle of four workshops linked by weekly peer support meetings">
    <circle cx="156" cy="57" r="51" fill="#7fc13d" opacity=".9"/>
    <text class="ws-label" x="156" y="46">Workshop 1</text>
    <text class="ws-name" x="156" y="63">-INSIGHT-</text>
    <text class="ws-hours" x="156" y="78">(5 hours)</text>

    <circle cx="265" cy="150" r="51" fill="#4a90c4"/>
    <text class="ws-label" x="265" y="139">Workshop 2</text>
    <text class="ws-name" x="265" y="156">-DESIGN-</text>
    <text class="ws-hours" x="265" y="171">(5 hours)</text>

    <circle cx="156" cy="244" r="51" fill="#e07b39"/>
    <text class="ws-label" x="156" y="233">Workshop 3</text>
    <text class="ws-name" x="156" y="250">-EXECUTE-</text>
    <text class="ws-hours" x="156" y="265">(5 hours)</text>

    <circle cx="56" cy="151" r="51" fill="#b9b6b4" opacity=".9"/>
    <text class="ws-label" x="56" y="140">Workshop 4</text>
    <text class="ws-name" x="56" y="157">-PRESENT-</text>
    <text class="ws-hours" x="56" y="172">(5 hours)</text>

    <g stroke-width="1.5" stroke-linejoin="round">
      <polygon points="0,-4 12,-4 12,-10 22,0 12,10 12,4 0,4" fill="#f3f0e8" stroke="#c9c6b8" transform="translate(93,89) rotate(-45) translate(-11,0)"/>
      <polygon points="0,-4 12,-4 12,-10 22,0 12,10 12,4 0,4" fill="#b6de5a" stroke="#8cc53f" transform="translate(216,95) rotate(45) translate(-11,0)"/>
      <polygon points="0,-4 12,-4 12,-10 22,0 12,10 12,4 0,4" fill="#a9d0ee" stroke="#4a90c4" transform="translate(219,206) rotate(135) translate(-11,0)"/>
      <polygon points="0,-4 12,-4 12,-10 22,0 12,10 12,4 0,4" fill="#f6b58a" stroke="#e07b39" transform="translate(93,212) rotate(-135) translate(-11,0)"/>
    </g>

    <text class="wps" x="17" y="80">WPS meetings</text>
    <text class="wps" x="217" y="77">Weekly Peer Support</text>
    <text class="wps" x="229" y="91">(WPS) meetings</text>
    <text class="wps" x="17" y="248">WPS meetings</text>
    <text class="wps" x="226" y="248">WPS meetings</text>
  </svg>

  <h3 class="section-title section-title--why">Why</h3>
  <h3 class="section-title section-title--how">How</h3>

  <div class="prose prose--why">
    <p>Many people are not entirely satisfied with their work, but they don’t know what to doabout it. The Tranquil Venture Course offers an opportunity, a safe place, a collective journey to help you reflect, design, and (very likely) do something about it.</p>
    <p class="lead">By the end of the Program, you should have:</p>
    <p class="list">1) Increased awareness, clarity and confidence<br>2) A deeper insight on what makes you happier and what you want<br>3) A clear design integrating your intended work and life<br>4) Initiated the execution of this design.</p>
  </div>

  <div class="prose prose--how">
    <p class="center">This Program differs from existing entrepreneurial programs in many ways:</p>
    <p>1) It starts upstream with mindfulness and self analysis to look deeply into yourself<br>2) Design and execution decisions are rooted on happiness rather than (only) financials<br>3) The process is holistic and inclusive, aiming at designing an integrated work and life, and on building synergies between your different parts.</p>
    <p class="format">The Program format includes lectures, individual work, group sharing, guided activities, experiential exercises, video, audio, handouts and other resources.</p>
  </div>
</section>

</body>
</html>
```